TRV Advisory Business Cards

Hi there,

I'd like to make a simple new business card design with the logo we already have created for our business.

I need a double sided business card with our logo on the front side and the company and person's details on the back side.

I'd like it to be on a white background and no background so I can potentially use it with either white paper or put it on different coloured paper in accordance with our business colours.

Please use the logo images I have attached and also the fonts.

So Front side:
- Logo in centre of business card (use medium logo so there is a pretty decent border around it, so don't want to fill the whole card but to make it prominent).

Back Side.
- We need 3 different business cards with the different people's name on each.

ie.

Dariel Moratkin
Business Development Manager

m +61 437 290 618
e dariel@trvadvisory.com.au
w trvadvisory.com.au

- Also I'd like to put only the cog/power button logo in the top right hand corner of the card.
(You might need to chop the current logo in half as I don't have a seperate log just for this)
- Also I'd like some lines running on the top left hand corner diagonally, anything that will add to the design or some swirling lines that add some cool effect to the card.

Also I'd like to maybe put our ABN in the bottom right hand corner of the card in a smaller font.

I'd like to also talk to the designer if possible so I can get my idea across a bit better.

Thanks!

Regards,
Dariel

```html
<!DOCTYPE html>
<html lang="en">
<head>
<meta charset="utf-8">
<title>TRV Advisory Business Cards</title>
<link rel="stylesheet" href="https://fonts.googleapis.com/css2?family=Questrial&display=swap">
<style>
  :root {
    --page: #e9e6e1;
    --card: #ffffff;
    --charcoal: #4a4a4c;
    --orange: #f39a1e;
    --ink: #3b3b3d;
    --shadow: rgba(0, 0, 0, 0.18);
  }
  * { box-sizing: border-box; margin: 0; padding: 0; }
  html, body {
    width: 1200px;
    height: 784px;
    overflow: hidden;
    background: var(--page);
    font-family: "Questrial", "Century Gothic", sans-serif;
  }
  .sheet {
    width: 1200px;
    height: 784px;
    display: flex;
    align-items: center;
    justify-content: space-evenly;
  }
  .card {
    position: relative;
    width: 540px;
    height: 309px;
    background: var(--card);
    overflow: hidden;
    box-shadow: 0 6px 18px var(--shadow);
  }

  /* Back side: contact details */
  .card-back .corner-disc {
    position: absolute;
    width: 300px;
    height: 300px;
    border-radius: 50%;
    background: var(--charcoal);
    right: -80px;
    top: -120px;
  }
  .person {
    position: absolute;
    left: 48px;
    top: 100px;
  }
  .person-name {
    color: var(--orange);
    font-size: 19px;
    letter-spacing: 0.2px;
  }
  .person-role {
    color: var(--ink);
    font-size: 12.5px;
    margin-top: 4px;
  }
  .contact-list {
    position: absolute;
    left: 48px;
    top: 190px;
    list-style: none;
  }
  .contact-item {
    display: flex;
    align-items: center;
    gap: 8px;
    color: var(--ink);
    font-size: 16px;
    line-height: 23px;
  }
  .contact-icon { width: 15px; height: 15px; flex: none; }

  /* Front side: company name */
  .brand {
    position: absolute;
    left: 0;
    right: 0;
    top: 104px;
    display: flex;
    align-items: center;
    justify-content: center;
    gap: 14px;
  }
  .brand-dot {
    width: 58px;
    height: 58px;
    border-radius: 50%;
    background: var(--orange);
  }
  .brand-name {
    color: var(--charcoal);
    font-size: 46px;
    letter-spacing: -0.5px;
  }
  .base-rule {
    position: absolute;
    left: 0;
    right: 0;
    bottom: 50px;
    height: 3px;
    background: var(--orange);
  }
  .base-band {
    position: absolute;
    left: 0;
    right: 0;
    bottom: 0;
    height: 44px;
    background: var(--charcoal);
  }
</style>
</head>
<body>
<main class="sheet">

  <section class="card card-back" aria-label="Business card, back">
    <div class="corner-disc"></div>
    <div class="person">
      <p class="person-name">Dariel Moratkin</p>
      <p class="person-role">Business Development Manager</p>
    </div>
    <ul class="contact-list">
      <li class="contact-item">
        <svg class="contact-icon" viewBox="0 0 16 16" aria-hidden="true">
          <path fill="#f39a1e" d="M3.6 1.5 6 4.2 4.7 5.9c.9 1.9 2.4 3.4 4.3 4.3l1.7-1.3 2.7 2.4-1.3 2.2C6.8 13.6 2.4 9.2 1.5 3z"/>
        </svg>
        +61 437 290 618
      </li>
      <li class="contact-item">
        <svg class="contact-icon" viewBox="0 0 16 16" aria-hidden="true">
          <rect x="1" y="3.5" width="14" height="9.5" rx="1.5" fill="#f39a1e"/>
          <path d="M1.8 4.5 8 9l6.2-4.5" fill="none" stroke="#fff" stroke-width="1.3"/>
        </svg>
        dariel@trvadvisory.com.au
      </li>
      <li class="contact-item">
        <svg class="contact-icon" viewBox="0 0 16 16" aria-hidden="true">
          <circle cx="8" cy="8" r="6.8" fill="#f39a1e"/>
          <g fill="none" stroke="#fff" stroke-width="1">
            <ellipse cx="8" cy="8" rx="2.8" ry="6.8"/>
            <path d="M1.2 8h13.6M2.5 4.6h11M2.5 11.4h11"/>
          </g>
        </svg>
        trvadvisory.com.au
      </li>
    </ul>
  </section>

  <section class="card card-front" aria-label="Business card, front">
    <div class="brand">
      <span class="brand-dot"></span>
      <span class="brand-name">TRV Advisory</span>
    </div>
    <div class="base-rule"></div>
    <div class="base-band"></div>
  </section>

</main>
</body>
</html>
```